Verdant Loop Advisors, LLC

I am looking for a simple, clear layout with my logo prominent and embossed, on the best quality card stock available. I would like the business name and phone number included on the card as well......I dont want my name anywhere on the card and I would like my logo embossed on the card......something simple with a white back......open to designs as long as they go along with recycling symbols and green type stuff.....The address, website, cell number, fax number, and email are listed below

5374 Tillbury Fenwood Road
Fenwood Hollow, ST 00000

c. 240.555.0143 f. 240.555.0187
e. sales@verdantloopadvisors.example
w. www.verdantloopadvisors.example

Industry/Entity Type

Recycling

```html
<!DOCTYPE html>
<html lang="en">
<head>
<meta charset="utf-8">
<title>Verdant Loop Advisors, LLC — Business Card</title>
<link href="https://fonts.googleapis.com/css2?family=Arimo:wght@400;700&display=swap" rel="stylesheet">
<style>
  :root {
    --backdrop: #2a2a2c;
    --card-black: #0c0c0d;
    --card-edge: #1a1a1b;
    --text-white: #f4f4f4;
    --accent-green: #2fa84f;
    --gloss-light: #9a9a9c;
    --gloss-dark: #141415;
  }
  * { margin: 0; padding: 0; box-sizing: border-box; }
  html, body {
    width: 1200px;
    height: 800px;
    overflow: hidden;
    background: var(--backdrop);
  }
  .canvas {
    position: relative;
    width: 1200px;
    height: 800px;
    background: var(--backdrop);
  }
  .business-card {
    position: absolute;
    left: 180px;
    top: 160px;
    width: 840px;
    height: 480px;
    background: radial-gradient(ellipse at 70% 40%, var(--card-edge) 0%, var(--card-black) 70%);
    overflow: hidden;
    font-family: "Arimo", Arial, sans-serif;
    color: var(--text-white);
  }
  .emblem-area {
    position: absolute;
    left: 0;
    top: 0;
    width: 330px;
    height: 480px;
    background: linear-gradient(135deg, var(--gloss-dark) 0%, var(--gloss-light) 30%, var(--gloss-dark) 55%, #5a5a5c 78%, var(--gloss-dark) 100%);
    opacity: 0.85;
  }
  .brand-name {
    position: absolute;
    left: 420px;
    top: 92px;
    display: flex;
    align-items: center;
    gap: 14px;
  }
  .brand-dot {
    width: 34px;
    height: 34px;
    border-radius: 50%;
    background: var(--accent-green);
    flex: none;
  }
  .brand-text {
    font-weight: 700;
    font-size: 27px;
    letter-spacing: 1px;
    text-transform: uppercase;
    color: var(--text-white);
    line-height: 1.15;
  }
  .contact-list {
    position: absolute;
    right: 48px;
    top: 262px;
    list-style: none;
    text-align: right;
  }
  .contact-line {
    display: flex;
    justify-content: flex-end;
    align-items: center;
    gap: 12px;
    font-size: 20px;
    letter-spacing: 0.6px;
    line-height: 30px;
    height: 30px;
    white-space: nowrap;
  }
  .contact-icon {
    width: 17px;
    height: 17px;
    flex: none;
    fill: var(--accent-green);
  }
  .icon-spacer { width: 17px; flex: none; }
</style>
</head>
<body>
<main class="canvas">
  <section class="business-card" aria-label="Verdant Loop Advisors business card">
    <div class="emblem-area" role="img" aria-label="Large glossy embossed recycling emblem in spot varnish"></div>

    <div class="brand-name">
      <span class="brand-dot" aria-hidden="true"></span>
      <span class="brand-text">Verdant Loop<br>Advisors, LLC</span>
    </div>

    <ul class="contact-list">
      <li class="contact-line">5374 Tillbury Fenwood Road<span class="icon-spacer"></span></li>
      <li class="contact-line">Fenwood Hollow, ST 00000
        <svg class="contact-icon" viewBox="0 0 24 24" aria-label="address"><path d="M12 2a7 7 0 0 0-7 7c0 5 7 13 7 13s7-8 7-13a7 7 0 0 0-7-7zm0 9.5A2.5 2.5 0 1 1 12 6.5a2.5 2.5 0 0 1 0 5z"/></svg>
      </li>
      <li class="contact-line">555.555.0143
        <svg class="contact-icon" viewBox="0 0 24 24" aria-label="phone"><path d="M6.6 10.8a15 15 0 0 0 6.6 6.6l2.2-2.2a1 1 0 0 1 1-.25 11.4 11.4 0 0 0 3.6.57 1 1 0 0 1 1 1V20a1 1 0 0 1-1 1A17 17 0 0 1 3 4a1 1 0 0 1 1-1h3.5a1 1 0 0 1 1 1c0 1.25.2 2.45.57 3.6a1 1 0 0 1-.25 1z"/></svg>
      </li>
      <li class="contact-line">555.555.0187
        <svg class="contact-icon" viewBox="0 0 24 24" aria-label="fax"><path d="M7 3h10v4H7zM4 8h16a2 2 0 0 1 2 2v6h-4v5H6v-5H2v-6a2 2 0 0 1 2-2zm4 8v3h8v-3z"/></svg>
      </li>
      <li class="contact-line">sales@verdantloopadvisors.example
        <svg class="contact-icon" viewBox="0 0 24 24" aria-label="email"><path d="M3 5h18a1 1 0 0 1 1 1v12a1 1 0 0 1-1 1H3a1 1 0 0 1-1-1V6a1 1 0 0 1 1-1zm1 2.2V17h16V7.2l-8 5.3z M4.6 7h14.8L12 11.9z"/></svg>
      </li>
      <li class="contact-line">www.verdantloopadvisors.example
        <svg class="contact-icon" viewBox="0 0 24 24" aria-label="website"><path d="M12 2a10 10 0 1 0 0 20 10 10 0 0 0 0-20zm6.9 9h-3a15 15 0 0 0-1.3-5.6A8 8 0 0 1 18.9 11zM12 4.1c.9 1.2 1.8 3.6 1.9 6.9h-3.8c.1-3.3 1-5.7 1.9-6.9zM9.4 5.4A15 15 0 0 0 8.1 11h-3a8 8 0 0 1 4.3-5.6zM5.1 13h3a15 15 0 0 0 1.3 5.6A8 8 0 0 1 5.1 13zm6.9 6.9c-.9-1.2-1.8-3.6-1.9-6.9h3.8c-.1 3.3-1 5.7-1.9 6.9zm2.6-1.3a15 15 0 0 0 1.3-5.6h3a8 8 0 0 1-4.3 5.6z"/></svg>
      </li>
    </ul>
  </section>
</main>
</body>
</html>
```